New Hotel Showcase Website

We plan to launch a website called www.brindlestays.net which showcases the world’s best new hotels. We want a mock up for 2 pages: the homepage (page 1) and the individual hotel page (page 2). We are looking for a design which combines simplicity while highlighting images/features of the hotel. Because the theme of the site is new hotels it is important that the design somehow emphasizes the age of each hotel listed – both on the homepage and then on the individual hotel page.

NOTE: WE WANT A CREATIVE, NEW APPROACH TO DISPLAYING HOTELS. NOT JUST A COPY OF CURRENT HOTEL WEBSITES.

The design should consider unique and creative ways of helping users to navigate the homepage (page 1) based on the age, location or style of the hotel they are interested in. The individual hotel page(page 2) can be more standard by clearly setting out hotel photos, feature lists, reviews, contact details and potential discounts. There is no booking system needed as this is not a hotel booking website.

The design should ideally be compatible with a content management system such as Page Loom. In terms of reference materials we like sites similar to:

http://www.velmarquay.net
http://www.corvidandpine.net
http://www.tessarooms.net
http://www.quillbeds.net

These sites are designed far more simply than large booking sites such as www.roamvix.net, www.bunkfold.net or even wander ledger. However, we are not looking for a copy of the above. We are looking for a design that presents hotels in a novel way and would be seen by the industry as a unique way of displaying new hotels.
Updates

Dear Designers - we have received quite a few entries already. Thank you. However, none of the designs submitted have responded to our brief. They are all copies or derivatives of current hotel websites which is not what we are looking for. We want (a) a new and creative approach to a hotel website and (b) one which creatively uses the age of the hotel (ie. 1 month old, 6 months old etc).

It will require creative thinking and new ideas. We wanted to challenge designers to come up with something new. Thanks.

```html
<!DOCTYPE html>
<html lang="en">
<head>
<meta charset="utf-8">
<title>Brindle Stays – New Hotels</title>
<link href="https://fonts.googleapis.com/css2?family=Nunito+Sans:wght@400;600;700&display=swap" rel="stylesheet">
<style>
:root{
  --green:#9dc43a;
  --orange:#f5821f;
  --navy:#3d5a8c;
  --ink:#4f566a;
  --muted:#6b7185;
  --faint:#a9adb9;
  --panel:#eff0f3;
  --rule:#d5d8e1;
  --slate:#6c7284;
}
*{box-sizing:border-box;margin:0;padding:0}
html,body{width:1200px;height:1000px;overflow:hidden}
body{font-family:"Nunito Sans",Arial,sans-serif;color:var(--ink);background:#fff;position:relative}
.abs{position:absolute}
.backdrop{left:0;top:20px;width:1200px;height:329px;background:linear-gradient(#fff 0%,#f3f4f7 40%,#e1e3ea 100%)}
.topbar{left:0;top:0;width:1200px;height:20px;background:var(--green);display:flex;justify-content:center;align-items:center;font-size:11px;color:#fff}
.topbar a{color:#fff;text-decoration:none;padding:0 19px;border-left:1px solid rgba(255,255,255,.4);line-height:9px;white-space:nowrap}
.topbar a:first-child{border-left:none}
.language{left:270px;top:58px;display:flex;align-items:center;font-size:10px;color:var(--muted)}
.language .select{margin-left:8px;width:68px;height:17px;border:1px solid #c9ccd5;background:#fff;font-size:10px;padding:1px 4px;position:relative;color:#444}
.language .select::after{content:"";position:absolute;right:0;top:0;width:15px;height:15px;border-left:1px solid #c9ccd5;background:linear-gradient(#fff,#e4e6eb)}
.language .select::before{content:"";position:absolute;right:4px;top:6px;border:3px solid transparent;border-top:4px solid #777;z-index:1}
.brand{left:440px;top:48px;width:320px;height:40px;white-space:nowrap;font-size:28px;line-height:40px;font-weight:400;color:var(--green);letter-spacing:1px;display:flex;align-items:center;justify-content:center;gap:8px}
.brand .mark{width:12px;height:12px;background:var(--orange);flex:none}
.follow{left:845px;top:58px;display:flex;align-items:center;gap:6px;font-size:10px;color:var(--muted)}
.follow .social{width:15px;height:15px;background:#b7bccb}
.filters{left:271px;top:109px;width:657px;height:35px;display:flex}
.filter{flex:1;color:#fff;font-size:13px;display:flex;align-items:center;padding-left:17px;position:relative;white-space:nowrap}
.filter b{margin-left:4px}
.filter svg{position:absolute;right:9px;top:8px}
.filter.age{background:var(--orange)}
.filter.location{background:var(--navy);border-left:1px solid #fff}
.filter.style{background:var(--green);border-left:1px solid #fff}
.stage-shape{left:200px;top:340px}
.hero{left:271px;top:144px;width:657px;height:286px;background:linear-gradient(135deg,#e9dcc4 0%,#b58a5a 35%,#6d3f24 65%,#3f4a2c 100%)}
.slide-btn{top:261px;width:41px;height:41px;background:var(--green);display:flex;align-items:center;justify-content:center}
.slide-btn.prev{left:264px}
.slide-btn.next{left:894px}
.feature{left:491px;top:479px;width:219px;height:68px;border-left:1px solid #c9ccd5;border-right:1px solid #c9ccd5;text-align:center}
.feature h1{font-size:18px;font-weight:700;color:var(--ink);line-height:20px;white-space:nowrap}
.feature .place{font-size:11px;color:var(--ink);margin-top:1px}
.feature .opened{font-size:11px;color:var(--faint);margin-top:4px}
.age-meter{display:flex;gap:3.6px;justify-content:center;margin-top:6px}
.age-meter span{width:10px;height:10px;background:#e4e6ec}
.age-meter span.on{background:var(--green)}
.age-meter span.half{background:linear-gradient(90deg,var(--green) 50%,#e4e6ec 50%)}
.intro{left:365px;top:565px;width:470px;text-align:center;font-size:10.8px;line-height:17.3px;color:var(--muted)}
.btn{background:var(--green);color:#fff;font-weight:700;font-size:11px;display:flex;align-items:center;justify-content:center;gap:6px;white-space:nowrap}
.btn::after{content:"";border:3.5px solid transparent;border-left:4px solid #fff;border-right:0}
.intro-btn{left:552px;top:626px;width:96px;height:24px}
.panel{top:691px;width:315px;height:139px}
.panel h2{font-size:16px;font-weight:400;color:var(--ink);height:34px;padding:6px 0 0 13px;border-bottom:1px solid var(--rule)}
.panel .body{background:var(--panel);height:104px;padding:12px 13px}
.panel.latest{left:271px;border-top:2px solid var(--orange)}
.panel.suggest{left:613px;border-top:2px solid var(--green)}
.latest .hotels{display:flex}
.latest .hotel{width:157px}
.latest .hotel + .hotel{border-left:1px solid #c9ccd5;padding-left:12px;margin-top:3px;height:60px}
.latest .hotel + .hotel h3{margin-top:-3px}
.latest h3{font-size:12px;font-weight:700;color:var(--ink);white-space:nowrap}
.latest .city{font-size:11px;color:var(--muted);margin-top:2px}
.latest .btn{width:90px;height:21px;margin-top:8px}
.latest .view-all{font-size:11px;color:var(--green);margin-top:6px}
.suggest p{font-size:10.4px;line-height:17px;color:var(--ink);letter-spacing:-.1px}
.suggest .fields{display:flex;gap:7px;margin-top:5px;font-size:11px;align-items:flex-end}
.suggest label{display:block;margin-bottom:3px;white-space:nowrap}
.suggest .input{width:117px;height:17px;border:1px solid #c9ccd5;background:#fff}
.suggest .send{width:41px;height:17px;background:var(--slate);color:#fff;font-size:9px;font-weight:700;display:flex;align-items:center;justify-content:center}
.footer-nav{left:271px;top:862px;width:657px;height:42px;border-top:1px solid var(--rule);border-bottom:1px solid var(--rule);display:flex;align-items:center}
.footer-nav a{font-size:9.5px;color:var(--green);text-decoration:none;margin-right:35px;white-space:nowrap}
.newsletter{margin-left:auto;display:flex;align-items:center;font-size:12px;color:var(--ink);white-space:nowrap}
.newsletter .input{width:137px;height:16px;border:1px solid #c9ccd5;margin:0 7px 0 10px;font-size:9px;padding:1px 5px;color:#555}
.newsletter .btn{width:62px;height:16px;font-size:9px}
.newsletter .btn::after{display:none}
.legal{left:330px;top:921px;width:540px;text-align:center;font-size:8.5px;line-height:14px;color:var(--muted)}
.copyright{left:0;top:957px;width:1200px;text-align:center;font-size:7px;color:var(--muted)}
</style>
</head>
<body>
<div class="abs backdrop"></div>

<nav class="abs topbar">
  <a>Home</a><a>About Us</a><a>Hotels</a><a>FAQs</a><a>Contact Us</a>
</nav>

<div class="abs language">Language <div class="select">English</div></div>
<div class="abs brand"><span class="mark"></span>BRINDLE STAYS</div>
<div class="abs follow">Follow us <span class="social"></span><span class="social"></span></div>

<div class="abs filters">
  <div class="filter age">Select <b>Age</b>
    <svg width="20" height="20" viewBox="0 0 20 20"><g fill="#fff" opacity=".55"><rect y="0" width="20" height="2"/><rect y="4" width="20" height="2"/><rect y="8" width="20" height="2"/></g><path d="M6 13h8l-4 4z" fill="#fff"/></svg></div>
  <div class="filter location">Select <b>Location</b>
    <svg width="20" height="20" viewBox="0 0 20 20"><g fill="#1e2d4c"><rect y="0" width="20" height="2"/><rect y="4" width="20" height="2"/><rect y="8" width="20" height="2"/></g><path d="M6 13h8l-4 4z" fill="#fff"/></svg></div>
  <div class="filter style">Select <b>Style</b>
    <svg width="20" height="20" viewBox="0 0 20 20"><g fill="#5f7f20" opacity=".8"><rect y="0" width="20" height="2"/><rect y="4" width="20" height="2"/><rect y="8" width="20" height="2"/></g><path d="M6 13h8l-4 4z" fill="#fff"/></svg></div>
</div>

<svg class="abs stage-shape" width="800" height="120" viewBox="0 0 800 120">
  <defs>
    <linearGradient id="sideShade" x1="0" y1="0" x2="0" y2="1"><stop offset="0" stop-color="#d9dce4"/><stop offset="1" stop-color="#fff" stop-opacity="0"/></linearGradient>
  </defs>
  <path d="M15 9 L71 9 L71 95 Z" fill="url(#sideShade)"/>
  <path d="M785 9 L728 9 L728 95 Z" fill="url(#sideShade)"/>
  <path d="M71 80 L728 80 L728 92 L400 117 L71 92 Z" fill="var(--rule)"/>
</svg>

<div class="abs hero" role="img" aria-label="Photo of a grand hotel lounge with marble columns, leather sofas and potted palms"></div>

<div class="abs slide-btn prev"><svg width="8" height="10" viewBox="0 0 8 10"><path d="M7 0v10L0 5z" fill="#fff"/></svg></div>
<div class="abs slide-btn next"><svg width="8" height="10" viewBox="0 0 8 10"><path d="M1 0v10l7-5z" fill="#fff"/></svg></div>

<section class="abs feature">
  <h1>The Ashcombe Park</h1>
  <div class="place">London . UK</div>
  <div class="opened">Opened 21 March 2013</div>
  <div class="age-meter"><span class="on"></span><span class="on"></span><span class="on"></span><span class="on"></span><span class="on"></span><span class="on"></span><span class="half"></span><span></span><span></span><span></span><span></span><span></span></div>
</section>

<p class="abs intro">Lorem ipsum dolor sit amet, consectetur adipisicing elit, sed do eiusmod tempor incididunt ut labore et dolore magna aliqua. Ut enim ad minim veniam, quis nostrud exercitation ullamco laboris nisi ut aliquip ex dolor sit amet tempor incididunt ut labore commodo consequat.</p>
<div class="abs btn intro-btn">Find out more</div>

<section class="abs panel latest">
  <h2>Latest hotels added</h2>
  <div class="body">
    <div class="hotels">
      <div class="hotel"><h3>Hotel Verdalina</h3><div class="city">Milan . Italy</div><div class="btn">Find out more</div></div>
      <div class="hotel"><h3>The Quayside Rest</h3><div class="city">Sidney . Australia</div><div class="btn">Find out more</div></div>
    </div>
    <div class="view-all">View all new hotels added</div>
  </div>
</section>

<section class="abs panel suggest">
  <h2>Suggest a hotel</h2>
  <div class="body">
    <p>Lorem ipsum dolor sit amet consectetur adipisicing elit, sed do eiusmod tempor incididunt ut labore et dolore magna:</p>
    <div class="fields">
      <div><label>Name of Hotel</label><div class="input"></div></div>
      <div><label>Location</label><div class="input"></div></div>
      <div class="send">Send</div>
    </div>
  </div>
</section>

<footer class="abs footer-nav">
  <a>Home</a><a>About Us</a><a>Hotels</a><a>FAQs</a><a>Contact Us</a>
  <div class="newsletter">Newsletter <div class="input">Enter your email address</div><div class="btn">Sign me up</div></div>
</footer>

<p class="abs legal">Any legal information in here ipsum dolor sit amet, consectetur adipisicing elit, sed do eiusmod tempor incididunt ut labore et dolore magna aliqua enim ad minim veniam, quis nostrud exercitation ullamco laboris nisi ut aliquip.</p>
<p class="abs copyright">© Copyright Brindle Stays . All rights reserved</p>
</body>
</html>
```